Emergency Vehicle Installer and Security Firm Needs a Business Card

Our company "Corvalt" need a business card for our Emergency Vehicle Equipment Installation and Infrastructure Security Business. We are contract designers, manufacturers and installers for Emergency Vehicle Fleets. This includes installation of Emergency Lights, Sirens, Vehicle Graphics and Radio Communications. We also supply this products to an international market. We also do consultant, and installation of high level security access, alarm and surveillance equipment for medium to large size businesses.

The design should represent a level of trust in our professionalism and expertise. It should visually display our ongoing relationship with the emergency services, but not overtake our commitment to high level security options.

Target Market(s)

Emergency Services and Businesses requiring high level security

Industry/Entity Type

Business

Contact Information for Business Card

*note complete details will be given to the winning designer for revising. The name "Mark Pell will be used to fill in name".

Mark Pell
Managing Director
Corvalt NZ Limited
Phone: +64 027 604 91352
Email: mark.pell@corvalt-example.co.nz

Requirements
Must have
• Card must be in black. Using our logo on the top as supplied. Designers should try having the reverse side as a blurred image of police lights (red and blue) with our logo in greyscale in the centre (this is not particularly a requirement, but feel free to play around with this option).
Nice to have
• A card design that looks good when spot UV printed. A clean compact and graphic design. A grey scale feel on the front (excluding logo, but you can play around with that idea). Rounded smooth text.
Should not have
• Will update this section as designs come through - feel free to submit what you feel would look good.

```html
<!DOCTYPE html>
<html lang="en">
<head>
<meta charset="utf-8">
<title>Corvalt Business Card</title>
<link href="https://fonts.googleapis.com/css2?family=Lato:wght@400;700;900&display=swap" rel="stylesheet">
<style>
  :root {
    --ink: #0a0a0a;
    --paper: #ffffff;
    --signal-red: #e41e26;
    --text-dark: #1c1c1c;
    --stage: #e9e7e3;
  }
  * { margin: 0; padding: 0; box-sizing: border-box; }
  html, body {
    width: 1200px; height: 900px; overflow: hidden;
    background: var(--stage);
    font-family: "Lato", sans-serif;
  }
  .stage {
    width: 1200px; height: 900px;
    display: flex; align-items: center; justify-content: center; gap: 40px;
  }
  .card {
    position: relative;
    width: 560px; height: 320px;
    border-radius: 24px;
    overflow: hidden;
    background: var(--ink);
    box-shadow: 0 10px 28px rgba(0,0,0,0.25);
  }
  .card-shape { position: absolute; inset: 0; }
  .brand {
    position: absolute;
    display: flex; align-items: center; gap: 12px;
    color: var(--paper);
    font-weight: 900;
    letter-spacing: 1px;
    text-transform: uppercase;
  }
  .brand-dot {
    background: var(--signal-red);
    border-radius: 50%;
    flex: none;
  }
  /* contact side */
  .contact .brand { left: 34px; top: 108px; font-size: 40px; }
  .contact .brand-dot { width: 18px; height: 18px; }
  .details {
    position: absolute; right: 26px; top: 40px;
    text-align: right; color: var(--text-dark);
  }
  .person-name { font-size: 30px; font-weight: 900; line-height: 1; }
  .person-name .surname { color: var(--signal-red); }
  .person-role { font-size: 14px; font-weight: 700; margin-top: 4px; }
  .contact-list { list-style: none; margin-top: 34px; }
  .contact-list li {
    display: flex; justify-content: flex-end; align-items: center; gap: 10px;
    font-size: 15px; line-height: 25px;
  }
  .contact-list svg { width: 16px; height: 16px; flex: none; }
  /* logo side */
  .front .brand {
    left: 0; right: 0; top: 118px; justify-content: center;
    font-size: 64px;
  }
  .front .brand-dot { width: 26px; height: 26px; }
  .front-web {
    position: absolute; left: 64px; top: 224px;
    color: var(--signal-red); font-size: 14px;
  }
</style>
</head>
<body>
<main class="stage">
  <article class="card contact">
    <svg class="card-shape" viewBox="0 0 560 320" aria-hidden="true">
      <path d="M318,0 Q205,150 178,320 L560,320 L560,0 Z" fill="var(--signal-red)"/>
      <path d="M340,0 Q225,155 200,320 L560,320 L560,0 Z" fill="var(--paper)"/>
    </svg>
    <div class="brand"><span class="brand-name">Corvalt</span><span class="brand-dot"></span></div>
    <div class="details">
      <p class="person-name">Mark <span class="surname">Pell</span></p>
      <p class="person-role">Managing Director</p>
      <ul class="contact-list">
        <li>+64 027 604 91352
          <svg viewBox="0 0 16 16"><path d="M4 1 L6.5 4.5 L5 6.5 Q7 10 9.5 11 L11.5 9.5 L15 12 L13 15 Q5 14 1 3 Z" fill="var(--signal-red)"/></svg></li>
        <li>mark.pell@corvalt-example.co.nz
          <svg viewBox="0 0 16 16"><rect x="1" y="3" width="14" height="10" fill="var(--signal-red)"/><path d="M1 3 L8 9 L15 3" stroke="#fff" stroke-width="1.4" fill="none"/></svg></li>
        <li>www.corvalt-example.co.nz
          <svg viewBox="0 0 16 16"><circle cx="8" cy="8" r="6.5" stroke="var(--signal-red)" stroke-width="1.5" fill="none"/><ellipse cx="8" cy="8" rx="3" ry="6.5" stroke="var(--signal-red)" stroke-width="1.2" fill="none"/><path d="M1.5 8 H14.5" stroke="var(--signal-red)" stroke-width="1.2"/></svg></li>
        <li>2480 Harlow Rd<span style="width:16px"></span></li>
        <li>Kestrel, nz 55102
          <svg viewBox="0 0 16 16"><path d="M8 15 Q2 8 2 6 A6 6 0 0 1 14 6 Q14 8 8 15 Z" fill="var(--signal-red)"/><circle cx="8" cy="6" r="2.2" fill="#fff"/></svg></li>
      </ul>
    </div>
  </article>

  <article class="card front">
    <div class="brand"><span class="brand-name">Corvalt</span><span class="brand-dot"></span></div>
    <p class="front-web">www.corvalt-example.co.nz</p>
  </article>
</main>
</body>
</html>
```